TalkBridge - Language Coaching Services

Sleek, innovative, trendy design for Language Coaching business.

TalkBridge is a new UK based company that provides Language Coaching services. We offer highly personalized on-line and face to face language courses. We also impart learning techniques workshops based on the latest neuroscience research for second-language acquisition.

Target Market(s)

Industry/Entity Type

Consulting

Contact Information for Business Card

TalkBridge
ElenaVT@talkbridge-demo.co.uk
TalkBridge-demo.co.uk
London, UK

Font styles to use
Sans Serif

```html
<!DOCTYPE html>
<html lang="en">
<head>
<meta charset="utf-8">
<title>TalkBridge – Business Card</title>
<link rel="stylesheet" href="https://fonts.googleapis.com/css2?family=Montserrat:wght@400;500;600&display=swap">
<style>
  :root {
    --page-bg: #1b1c1e;
    --card-bg: #2b2e32;
    --card-edge: #36393e;
    --brand-blue: #2fa4c9;
    --text-light: #f2f4f5;
    --text-soft: #c4cbd0;
    --text-muted: #9aa3a9;
  }
  * { margin: 0; padding: 0; box-sizing: border-box; }
  html, body {
    width: 1200px;
    height: 1200px;
    overflow: hidden;
    background: var(--page-bg);
    font-family: "Montserrat", sans-serif;
  }
  .sheet {
    width: 1200px;
    height: 1200px;
    display: flex;
    flex-direction: column;
    align-items: center;
    justify-content: center;
    gap: 60px;
  }
  .card {
    width: 840px;
    height: 480px;
    background: radial-gradient(circle at 40% 30%, #33373c 0%, var(--card-bg) 60%, #25282b 100%);
    border: 1px solid var(--card-edge);
    border-radius: 4px;
    box-shadow: 0 18px 40px rgba(0,0,0,.45);
    display: flex;
    flex-direction: column;
    align-items: center;
    color: var(--text-light);
  }
  .card--front { justify-content: center; padding-top: 20px; }
  .brand-mark {
    width: 150px;
    height: 150px;
    border: 9px solid var(--brand-blue);
    border-radius: 50%;
  }
  .brand-name {
    margin-top: 26px;
    font-size: 62px;
    font-weight: 500;
    letter-spacing: 3px;
    text-transform: uppercase;
    color: var(--brand-blue);
  }
  .tagline {
    margin-top: 50px;
    font-size: 19px;
    font-weight: 400;
    letter-spacing: .6px;
    color: var(--text-light);
  }
  .card--back { justify-content: center; }
  .card--back .brand-mark { width: 160px; height: 160px; }
  .contact {
    margin-top: 30px;
    text-align: center;
    font-style: normal;
    line-height: 1.45;
  }
  .contact__name { font-size: 24px; font-weight: 600; color: var(--text-light); }
  .contact__email { font-size: 23px; color: var(--text-soft); }
  .contact__web { font-size: 23px; color: var(--text-soft); }
  .contact__city { font-size: 23px; color: var(--text-muted); }
</style>
</head>
<body>
  <main class="sheet">
    <section class="card card--front" aria-label="Business card front">
      <div class="brand-mark" aria-hidden="true"></div>
      <h1 class="brand-name">TalkBridge</h1>
      <p class="tagline">We offer highly customized coaching sessions and self-study content</p>
    </section>
    <section class="card card--back" aria-label="Business card back">
      <div class="brand-mark" aria-hidden="true"></div>
      <address class="contact">
        <div class="contact__name">TalkBridge</div>
        <div class="contact__email">ElenaVT@talkbridge-demo.co.uk</div>
        <div class="contact__web">TalkBridge-demo.co.uk</div>
        <div class="contact__city">London, UK</div>
      </address>
    </section>
  </main>
</body>
</html>
```